Revamp Existing Business Card Into a Modern Clean Design

See ATTACHED detailed instructions on design, color and business card examples shown to point you into the right direction.

Good luck and May The Force Be With You. :D

```html
<!DOCTYPE html>
<html lang="en">
<head>
<meta charset="utf-8">
<title>Roving Capitol Notary – Business Card</title>
<link href="https://fonts.googleapis.com/css2?family=Questrial&display=swap" rel="stylesheet">
<style>
  :root{
    --page:#e8e3da;
    --blue:#1f6fc0;
    --blue-deep:#124f96;
    --blue-light:#5aa6e6;
    --blue-pale:#cfe4f7;
    --white:#ffffff;
    --ink:#2d5d93;
    --grey:#7a8594;
  }
  *{box-sizing:border-box;margin:0;padding:0}
  html,body{width:1200px;height:1023px;overflow:hidden}
  body{background:var(--page);font-family:"Questrial",sans-serif;position:relative}
  .card{position:absolute;top:172px;width:390px;height:680px;border-radius:18px;overflow:hidden;background:var(--white);box-shadow:0 6px 18px rgba(0,0,0,.18)}
  .card--front{left:170px}
  .card--back{left:640px}
  .card__bg{position:absolute;inset:0}

  .brand{position:absolute;top:58px;right:26px;display:flex;align-items:center;gap:8px;color:var(--blue);font-size:19px;line-height:1.05;text-align:right}
  .brand__dot{width:26px;height:26px;border-radius:50%;background:var(--blue)}

  .contacts{position:absolute;top:150px;left:30px;list-style:none;color:var(--grey);font-size:13.5px}
  .contacts li{display:flex;align-items:center;gap:10px;height:25px}
  .contacts .ico{width:17px;height:17px;border-radius:50%;background:var(--ink);flex:none;display:flex;align-items:center;justify-content:center}
  .contacts .ico svg{width:10px;height:10px}
  .contacts .addr{padding-left:27px}

  .payment__title{position:absolute;top:488px;left:0;width:100%;text-align:center;color:var(--white);font-size:19px;letter-spacing:.5px}
  .payment__grid{position:absolute;top:530px;left:24px;right:24px;display:grid;grid-template-columns:repeat(4,1fr);gap:16px 12px}
  .pay{height:40px;border-radius:7px;background:var(--white);color:var(--blue);display:flex;align-items:center;justify-content:center;font-size:14px;box-shadow:0 2px 4px rgba(0,0,0,.18)}
  .pay--solid{background:var(--blue-deep);color:var(--white)}

  .map{position:absolute;top:150px;left:150px;width:240px;height:230px;border-radius:40% 0 0 50%;background:radial-gradient(ellipse at center,rgba(90,166,230,.55),rgba(90,166,230,0) 70%)}
  .intro{position:absolute;top:34px;left:26px;right:24px;color:var(--white);font-size:13.5px;line-height:1.3}
  .services{position:absolute;top:108px;left:24px;right:18px;list-style:none;color:var(--white);font-size:13.5px;line-height:1.2}
  .services li{display:flex;align-items:flex-start;gap:12px;margin-bottom:11px}
  .services .badge{width:26px;height:26px;border-radius:50%;background:var(--blue-pale);border:2px solid var(--white);flex:none}

  .clients{position:absolute;top:465px;left:26px;width:260px;display:grid;grid-template-columns:1fr 1fr;gap:14px 10px;color:var(--blue-deep);font-size:15px}
  .clients span{white-space:nowrap}
  .clients__label{position:absolute;right:24px;bottom:40px;color:var(--blue-deep);font-size:14px;line-height:1.35;text-align:left;display:flex;gap:8px;align-items:flex-start}
  .clients__label svg{margin-top:4px}
</style>
</head>
<body>

<section class="card card--front" aria-label="Card front">
  <svg class="card__bg" viewBox="0 0 390 680" aria-hidden="true">
    <defs>
      <linearGradient id="bandGrad" x1="0" y1="0" x2="1" y2="1">
        <stop offset="0" stop-color="#124f96"/><stop offset="1" stop-color="#3f93dc"/>
      </linearGradient>
    </defs>
    <path d="M0,0 H390 V22 C260,26 110,70 0,140 Z" fill="url(#bandGrad)"/>
    <path d="M0,0 H390 V10 C260,14 110,52 0,118 Z" fill="#5aa6e6" opacity=".5"/>
    <path d="M0,430 C120,400 260,380 390,330 V680 H0 Z" fill="#5aa6e6" opacity=".55"/>
    <path d="M0,460 C130,430 270,410 390,365 V680 H0 Z" fill="url(#bandGrad)"/>
  </svg>

  <div class="brand"><span>Roving Capitol<br>Notary</span><span class="brand__dot"></span></div>

  <ul class="contacts">
    <li><span class="ico"><svg viewBox="0 0 10 10"><path d="M2,1 L4,1 L4.6,3 L3.5,3.8 C4,5 5,6 6.2,6.5 L7,5.4 L9,6 L9,8 C5,8.5 1.5,5 2,1 Z" fill="#fff"/></svg></span>512-555-0142</li>
    <li><span class="ico"><svg viewBox="0 0 10 10"><path d="M2,1 L4,1 L4.6,3 L3.5,3.8 C4,5 5,6 6.2,6.5 L7,5.4 L9,6 L9,8 C5,8.5 1.5,5 2,1 Z" fill="#fff"/></svg></span>512-555-0187</li>
    <li><span class="ico"><svg viewBox="0 0 10 10"><circle cx="5" cy="5" r="3.5" fill="none" stroke="#fff" stroke-width="1.2"/></svg></span>rovingcapitolnotary.com</li>
    <li><span class="ico"><svg viewBox="0 0 10 10"><rect x="1" y="2.5" width="8" height="5" fill="none" stroke="#fff" stroke-width="1"/><path d="M1,2.5 L5,5.5 L9,2.5" fill="none" stroke="#fff" stroke-width="1"/></svg></span>notary@rovingcapitolnotary.com</li>
    <li><span class="ico"></span>chirpnet.example/capitolnotary</li>
    <li><span class="ico"></span>pinboardly.example/capitolnotary</li>
    <li><span class="ico"></span>vidstream.example/rovingcapitolnotary</li>
    <li><span class="ico"></span>friendspace.example/rovingnotary</li>
    <li><span class="ico"><svg viewBox="0 0 10 10"><path d="M5,9.5 C3,6.5 2,5 2,3.8 A3,3 0 0 1 8,3.8 C8,5 7,6.5 5,9.5 Z" fill="#fff"/><circle cx="5" cy="3.8" r="1.1" fill="#2d5d93"/></svg></span>4100 Meadow Ridge Dr, Ste 210</li>
    <li class="addr">Austin, TX 78745</li>
  </ul>

  <p class="payment__title">We Accept For Payment</p>
  <div class="payment__grid">
    <span class="pay pay--solid">Vanta</span>
    <span class="pay">Meridian</span>
    <span class="pay">Novacard</span>
    <span class="pay">Keystone</span>
    <span class="pay pay--solid">Cash</span>
    <span class="pay pay--solid">Check</span>
    <span class="pay pay--solid">Debit</span>
    <span class="pay pay--solid">PayLoop</span>
  </div>
</section>

<section class="card card--back" aria-label="Card back">
  <svg class="card__bg" viewBox="0 0 390 680" aria-hidden="true">
    <defs>
      <linearGradient id="backGrad" x1="0" y1="0" x2="1" y2="1">
        <stop offset="0" stop-color="#3f93dc"/><stop offset="1" stop-color="#124f96"/>
      </linearGradient>
    </defs>
    <rect width="390" height="680" fill="url(#backGrad)"/>
    <path d="M0,448 C140,420 270,400 390,345 V680 H0 Z" fill="#5aa6e6" opacity=".6"/>
    <path d="M0,462 C140,436 270,418 390,366 V680 H0 Z" fill="#ffffff"/>
  </svg>

  <div class="map" role="img" aria-label="Faint world map behind the services list"></div>

  <p class="intro">Roving Capitol Notary provides these services anywhere in Texas to companies and individuals located anywhere in the world...</p>

  <ul class="services">
    <li><span class="badge"></span>Texas process server services</li>
    <li><span class="badge"></span>Texas loan signing agent services</li>
    <li><span class="badge"></span>Texas mobile notary public services</li>
    <li><span class="badge"></span>Texas Secretary of State rush apostille &amp; authentication services</li>
    <li><span class="badge"></span>U.S Department of State rush apostille &amp; authentication services</li>
    <li><span class="badge"></span>U.S Embassy &amp; Consulate rush document legalization services</li>
  </ul>

  <div class="clients">
    <span>Harlow Trust</span><span>Civica Bank</span>
    <span>Brandt Lyle</span><span></span>
    <span>Pemberton Chase</span><span>Fieldfresh</span>
    <span>Tallcart</span><span></span>
    <span>Corrin Petroleum</span><span>Ridgeline Oil</span>
  </div>

  <p class="clients__label">
    <svg width="9" height="10" viewBox="0 0 9 10" aria-hidden="true"><path d="M9,0 V10 L0,5 Z" fill="#124f96"/></svg>
    <span>SOME<br>OF OUR<br>CLIENTS</span>
  </p>
</section>

</body>
</html>
```